Web Design For Staffing Company

We need a homepage web design for a technical staffing company.

Please see attached brief for project details.

please make the site modern with bold colors while matching the logo

Be sure to read the attached breif in full beforehand.

Target Market(s)

technical companies looking to hire talent

Industry/Entity Type

Staffing

Number of Pages Required

1 page

Font styles to use
Sans Serif

```html
<!DOCTYPE html>
<html lang="en">
<head>
<meta charset="utf-8">
<title>Vantrex Staffing — Technical Staffing</title>
<link rel="stylesheet" href="https://fonts.googleapis.com/css2?family=Roboto:ital,wght@0,400;0,500;0,700;1,400&family=Roboto+Condensed:wght@700&display=swap">
<style>
:root{
  --blue:#3f95dd;
  --blue-dark:#2f7fc8;
  --ink:#1d2530;
  --text:#555b63;
  --line:#e3e6ea;
  --pale:#eaf3fb;
  --footer:#232323;
  --white:#fff;
  --star:#f5a623;
}
*{box-sizing:border-box;margin:0;padding:0}
html,body{width:1200px;height:3772px;overflow:hidden}
body{position:relative;background:var(--white);font-family:'Roboto',sans-serif;color:var(--ink)}
.abs{position:absolute}
.heading{font-family:'Roboto Condensed',sans-serif;font-weight:700}
.btn{position:absolute;display:flex;align-items:center;justify-content:center;font-size:14px;font-weight:700;letter-spacing:.3px;border-radius:4px;text-transform:uppercase}
.btn-outline{border:2px solid var(--ink);color:var(--ink);background:var(--white)}
.btn-solid{background:var(--blue);color:var(--white)}
.btn-white{background:var(--white);color:var(--blue)}

/* header */
.site-header{left:0;top:0;width:1200px;height:105px;background:var(--white)}
.brand{left:76px;top:30px;display:flex;align-items:center;gap:10px;font-size:30px;font-weight:700;color:var(--blue-dark)}
.brand-dot{width:22px;height:22px;border-radius:50%;background:var(--blue-dark)}
.nav a{position:absolute;top:44px;font-size:14px;font-weight:500;color:#3b4450;text-decoration:none}
.nav .active{color:var(--blue);padding-bottom:8px;border-bottom:2px solid var(--blue)}
.search{left:850px;top:28px;width:271px;height:51px;border:1px solid #cfd5db;border-radius:4px}
.search span{position:absolute;left:18px;top:17px;font-size:13px;color:#9aa1a8}
.search b{position:absolute;right:4px;top:4px;width:108px;height:41px;background:var(--blue);color:#fff;font-size:12px;font-weight:500;display:flex;align-items:center;justify-content:center;border-radius:3px}

/* hero */
.hero{left:0;top:105px;width:1200px;height:540px;background:linear-gradient(180deg,#e9e9e9 0%,#dcdcdc 45%,#5a5f66 72%,#1e2228 100%)}
.hero h1{position:absolute;left:0;top:140px;width:1200px;text-align:center;font-size:34px;color:#1b1f25}
.hero p{position:absolute;left:0;top:188px;width:1200px;text-align:center;font-size:20px;color:#2a2e35}
.hero-line{left:599px;top:645px;width:1px;height:48px;background:#8fa6bc}

.intro{left:205px;top:734px;width:790px;text-align:center;font-size:18px;font-weight:500;line-height:34px;color:#1b1f25}

.copy{font-size:13.5px;line-height:26px;color:var(--text)}
.photo{background:linear-gradient(135deg,#dfe8ef,#9db3c6 55%,#36475a)}
.soft-band{left:0;top:1560px;width:1200px;height:220px;background:linear-gradient(180deg,rgba(234,243,251,0) 0%,var(--pale) 60%,var(--pale) 100%)}

/* testimonials */
.testi-band{left:0;top:1780px;width:1200px;height:422px;background:linear-gradient(135deg,#3b8fd8,#2f82cc 60%,#3d95dd)}
.testi-title{left:0;top:1870px;width:1200px;text-align:center;font-size:33px;color:#fff}
.card-back{left:177px;top:1992px;width:846px;height:296px;background:#dedede}
.card{left:196px;top:1961px;width:806px;height:358px;background:#ececec;box-shadow:0 8px 18px rgba(0,0,0,.15)}
.avatar{left:565px;top:1981px;width:70px;height:70px;border-radius:50%;background:linear-gradient(160deg,#9cc8ee,#2f6fa8)}
.quote{left:232px;top:2059px;width:736px;text-align:center;font-style:italic;font-size:18px;line-height:34px;color:#5a5e63}
.stars{left:0;top:2212px;width:1200px;text-align:center}
.testi-name{left:0;top:2247px;width:1200px;text-align:center;font-size:18px;font-weight:500;color:var(--blue)}

/* blog */
.blog-title{left:0;top:2466px;width:1200px;text-align:center;font-size:34px;color:#1b1f25}
.post{position:absolute;top:2536px;width:305px;height:406px;border:1px solid var(--line);border-radius:4px;background:#fff}
.post .img{position:absolute;left:0;top:0;width:100%;height:190px}
.post .date{position:absolute;left:120px;top:158px;width:64px;height:64px;border-radius:50%;background:var(--blue);border:3px solid #fff;color:#fff;text-align:center;font-weight:500}
.post .date small{display:block;font-size:12px;margin-top:8px}
.post .date strong{display:block;font-size:22px;line-height:22px}
.post h3{position:absolute;left:30px;top:238px;width:245px;text-align:center;font-size:21px;font-weight:500;line-height:31px;color:#1b1f25}
.post p{position:absolute;left:36px;top:306px;width:233px;text-align:center;font-size:13px;line-height:26px;color:#6a7078}

/* cta */
.cta{position:absolute;top:3119px;width:477px;height:248px;background:linear-gradient(135deg,#2e7ec6,#3f95dd 50%,#3185cf)}
.cta h2{position:absolute;left:0;top:52px;width:100%;text-align:center;font-size:33px;line-height:43px;color:#fff}

/* footer */
.site-footer{left:0;top:3392px;width:1200px;height:380px;background:var(--footer)}
.fcol h4{position:absolute;top:92px;font-size:20px;font-weight:500;color:#fff}
.fcol p{position:absolute;top:124px;width:280px;font-size:14px;line-height:26px;color:#e6e6e6}
.fbtn{position:absolute;top:212px;width:200px;height:54px;background:var(--blue);color:#fff;border-radius:3px;display:flex;align-items:center;justify-content:center;gap:8px;font-size:14px;font-weight:700}
.fdivider{left:0;top:311px;width:1200px;height:1px;background:#3a3a3a}
.copyright{left:0;top:334px;width:1200px;text-align:center;font-size:14px;color:#e6e6e6}
</style>
</head>
<body>

<header class="abs site-header">
  <div class="abs brand"><span class="brand-dot"></span>Vantrex Staffing</div>
  <nav class="nav">
    <a class="active" style="left:363px">Home</a>
    <a style="left:445px">About</a>
    <a style="left:529px">Job Seekers</a>
    <a style="left:652px">Clients</a>
    <a style="left:741px">Contact</a>
  </nav>
  <div class="abs search"><span>Keyword &amp; Location</span><b>SEARCH JOBS</b></div>
</header>

<section class="abs hero" role="img" aria-label="Speaker presenting to a seated audience in front of a white brick wall">
  <h1 class="heading">The Right People For The Right Jobs!</h1>
  <p>Bridging the talent gap in Technical Staffing</p>
  <div class="btn btn-outline" style="left:447px;top:236px;width:143px;height:52px">Hire Talent</div>
  <div class="btn btn-solid" style="left:609px;top:236px;width:143px;height:52px">Get Hired</div>
</section>
<div class="abs hero-line"></div>

<p class="abs intro">Vantrex Staffing is a National Technical Staffing and Recruiting Solutions Provider founded in 2013 focused on matching contract and full time Engineering and IT professionals with new and exciting employment opportunities!</p>

<p class="abs copy" style="left:111px;top:958px;width:462px">Simply said... WE LOVE TO RECRUIT! It's our passion and we take it very seriously! It is not easy for JOB SEEKERS to put their job search efforts and trust in the hands of someone else, especially when there are so many Staffing Firms to choose from. So how do you know you are choosing the best Staffing Representation possible?</p>
<div class="btn btn-outline" style="left:111px;top:1118px;width:141px;height:50px">Learn More</div>
<div class="btn btn-solid" style="left:274px;top:1118px;width:142px;height:50px">View Jobs</div>
<div class="abs" style="left:598px;top:913px;width:533px;height:356px;background:linear-gradient(90deg,#fafbfc,#eef2f5 30%,#eef2f5 70%,#fafbfc)"></div>
<div class="abs photo" role="img" aria-label="Four business professionals walking across a glass bridge" style="left:688px;top:913px;width:360px;height:356px;border-radius:50%"></div>

<div class="abs soft-band"></div>
<div class="abs" role="img" aria-label="Team meeting around a conference table, tinted blue" style="left:164px;top:1318px;width:364px;height:364px;border-radius:50%;background:radial-gradient(circle at 45% 40%,#6eaee5,#3f8fd6 70%,#2f7fc8)"></div>
<div class="abs" style="left:274px;top:1480px;display:flex;align-items:center;gap:8px;font-size:32px;font-weight:700;color:#fff"><span style="width:20px;height:20px;border-radius:50%;background:#fff"></span>Vantrex</div>
<p class="abs copy" style="left:618px;top:1379px;width:466px">Are you responsible for Technical Staffing within your organization? Are you satisfied with your current Supplier(s)' overall performance? Does it appear they identify potential Candidate(s) based purely on "buzz-word" searches? Is it evident they just do not grasp the scope and responsibilities of your technical staffing need(s)?</p>
<div class="btn btn-outline" style="left:618px;top:1537px;width:142px;height:50px">Learn More</div>
<div class="btn btn-solid" style="left:781px;top:1537px;width:142px;height:50px">Hire Talent</div>

<section class="abs testi-band"></section>
<h2 class="abs heading testi-title">What Client Say About us?</h2>
<div class="abs card-back"></div>
<div class="abs card"></div>
<div class="abs avatar" role="img" aria-label="Client portrait"></div>
<p class="abs quote">"Dana Whitlow is an excellent recruiter. She is articulate, honest, has a good nature and is an effective information conduit between her clients and candidates. She gave me the feeling she is there for the big picture desiring to forge a future relationship that will be mutually beneficial to both of us."</p>
<svg class="abs stars" height="22" viewBox="0 0 1200 22" aria-label="5 stars">
  <g fill="var(--star)">
    <path id="star" d="M556 2l3 6.5 7 .8-5.2 4.8 1.4 7-6.2-3.6-6.2 3.6 1.4-7-5.2-4.8 7-.8z"/>
    <use href="#star" x="22"/><use href="#star" x="44"/><use href="#star" x="66"/><use href="#star" x="88"/>
  </g>
</svg>
<p class="abs testi-name">Sam R. - Electrical Test Engineer in the Automotive Sector:</p>
<svg class="abs" style="left:510px;top:2350px" width="180" height="26" viewBox="0 0 180 26" aria-label="Slider controls">
  <path d="M30 13H6M13 6l-7 7 7 7" stroke="#9aa0a6" stroke-width="2" fill="none"/>
  <circle cx="63" cy="13" r="7" fill="#d5d8dc"/><circle cx="89" cy="13" r="8" fill="var(--blue)"/><circle cx="115" cy="13" r="7" fill="#d5d8dc"/>
  <path d="M146 13h24M163 6l7 7-7 7" stroke="#222" stroke-width="2" fill="none"/>
</svg>

<h2 class="abs heading blog-title">Our Latest Blog</h2>
<article class="post" style="left:111px">
  <div class="img photo" role="img" aria-label="Professional woman on a phone call in an office"></div>
  <div class="date"><small>Jun</small><strong>19</strong></div>
  <h3>Tips for Spotting a U.S. Recession Before</h3>
  <p>As the U.S. nears a record-long expansion in July, the conversation is increasingly turning</p>
</article>
<article class="post" style="left:447px">
  <div class="img photo" role="img" aria-label="Two colleagues celebrating at a laptop"></div>
  <div class="date"><small>Jun</small><strong>17</strong></div>
  <h3>Ways To Make The Most<br>Of The Hot Job Market</h3>
  <p>"This is the tightest labor market I can remember. Unemployment is at a 50-year low and wage growth"</p>
</article>
<article class="post" style="left:784px">
  <div class="img photo" role="img" aria-label="Team meeting at an outdoor waterfront table"></div>
  <div class="date"><small>Jun</small><strong>06</strong></div>
  <h3>Meeting Employees'<br>Needs To Improve</h3>
  <p>The benefits of employee satisfaction are well-established, so HR professionals and leaders across</p>
</article>
<div class="btn btn-solid" style="left:507px;top:2970px;width:185px;height:49px">View More Blogs</div>

<section class="cta" style="left:111px">
  <h2 class="heading">Looking For Career-Mined<br>Candidates?</h2>
  <div class="btn btn-white" style="left:143px;top:151px;width:185px;height:50px">Request Talent</div>
</section>
<section class="cta" style="left:612px">
  <h2 class="heading" style="top:34px">Looking For Career<br>Opportunies?</h2>
  <div class="btn btn-white" style="left:142px;top:151px;width:185px;height:50px">Search Jobs</div>
</section>

<footer class="abs site-footer">
  <div class="fcol">
    <h4 style="left:110px">GET HIRED</h4>
    <p style="left:110px">Sed ut perspiciatis unde omnis iste natus error sit voluptatem accusantium dolo remque laudantium</p>
    <div class="fbtn" style="left:111px"><svg width="14" height="14" viewBox="0 0 14 14"><circle cx="6" cy="6" r="4.5" stroke="#fff" stroke-width="2" fill="none"/><path d="M9.5 9.5L13 13" stroke="#fff" stroke-width="2"/></svg>SEARCH NOW</div>
  </div>
  <div class="fcol">
    <h4 style="left:482px">HIRE TALENT</h4>
    <p style="left:482px">Sed ut perspiciatis unde omnis iste natus error sit voluptatem accusantium dolo remque laudantium</p>
    <div class="fbtn" style="left:483px"><svg width="14" height="14" viewBox="0 0 14 14"><circle cx="7" cy="7" r="6" stroke="#fff" stroke-width="1.6" fill="none"/><circle cx="7" cy="5.5" r="2" fill="#fff"/><path d="M3.5 11.5c1-2 6-2 7 0" stroke="#fff" stroke-width="1.6" fill="none"/></svg>START TODAY</div>
  </div>
  <div class="fcol">
    <h4 style="left:854px">GET IN TOUCH</h4>
    <p style="left:854px;width:300px">Vantrex Staffing, Inc.<br>204 Harbor Street, Bldg. 2, 3rd floor<br>Millbrook, MA 01770</p>
    <div class="fbtn" style="left:855px"><svg width="15" height="12" viewBox="0 0 15 12"><rect x="1" y="1" width="13" height="10" stroke="#fff" stroke-width="1.5" fill="none"/><path d="M1 1l6.5 5.5L14 1" stroke="#fff" stroke-width="1.5" fill="none"/></svg>CONTACT US</div>
  </div>
  <div class="abs fdivider"></div>
  <p class="abs copyright">© Copyrights 2020 | All Rights Reserved</p>
</footer>

</body>
</html>
```